Fernvale Craft Works business card design- Fine Art sculpture business (Contract guaranteed)

This business card is for a fine art business. Though we don't have a website up and running yet it should be up soon. I would like the business card to be elegant and fairly simple with a picture of one of my sculptures on the front (you might need to photoshop out the background) as well as my basic contact info (my name,phone # and e-mail). On the back I'd like it to be pretty simple with just "Notes" and some blank lines for writing in info.

Target Market(s)

High end artwork buyers

Industry/Entity Type

Art Gallery

Contact Information for Business Card

Marlo Prewitt Phone: (555) 213-4098 E-mail: marlo@quillbrookmail.com Facebook: @fernvalecraftworks Instagram: fernvalecraftworks

Colors

Designer to choose colors to be used in the design.

Requirements
Must have
• *A picture of one of my sculptures*, my name, business name (Fernvale Craft Works), e-mail, phone #, and a notes section on the back.
• Fernvale Craft Works
• Marlo Prewitt
• (555)213-4098
• marlo@quillbrookmail.com
• Facebook: @fernvalecraftworks
• Instagram: fernvalecraftworks
Nice to have
• It'd be nice if you can crop out the background in the sculpture pictures, which ever one you end up using.

```html
<!DOCTYPE html>
<html lang="en">
<head>
<meta charset="utf-8">
<title>Fernvale Craft Works – Business Card</title>
<link rel="stylesheet" href="https://fonts.googleapis.com/css2?family=Source+Serif+4:wght@300;700&family=Open+Sans:wght@400&family=Tinos:wght@700&display=swap">
<style>
  :root {
    --page-bg: #fbfcfd;
    --card-front: #130651;
    --contact-band: #220aa8;
    --card-back: #ffffff;
    --ink-light: #ffffff;
    --ink-dark: #14084f;
    --rule: #2a1a8a;
    --stone-deep: #2a1470;
    --stone-bright: #6a4fd8;
    --stone-base: #4d5a55;
  }
  * { margin: 0; padding: 0; box-sizing: border-box; }
  html, body {
    width: 1200px;
    height: 1200px;
    overflow: hidden;
    background: var(--page-bg);
  }
  .card {
    position: absolute;
    left: 180px;
    width: 840px;
    height: 480px;
  }
  .card--front {
    top: 85px;
    background: var(--card-front);
  }
  .card--back {
    top: 618px;
    background: var(--card-back);
  }
  .sculpture-photo {
    position: absolute;
    left: 54px;
    top: 27px;
    width: 198px;
    height: 400px;
    border-radius: 40% 45% 20% 20% / 30% 30% 10% 10%;
    background: linear-gradient(170deg, var(--stone-bright) 0%, var(--stone-deep) 55%, var(--stone-bright) 75%, var(--stone-base) 100%);
  }
  .identity {
    position: absolute;
    left: 313px;
    width: 400px;
    top: 148px;
    text-align: center;
    color: var(--ink-light);
  }
  .identity__name {
    font-family: "Source Serif 4", Georgia, serif;
    font-weight: 700;
    font-size: 39px;
    line-height: 1.2;
  }
  .identity__studio {
    font-family: "Source Serif 4", Georgia, serif;
    font-weight: 300;
    font-size: 38px;
    line-height: 1.3;
    margin-top: 2px;
  }
  .contact-band {
    position: absolute;
    left: 0;
    bottom: 0;
    width: 100%;
    height: 49px;
    background: var(--contact-band);
    color: var(--ink-light);
    font-family: "Open Sans", Arial, sans-serif;
    font-size: 27px;
    line-height: 49px;
    white-space: nowrap;
  }
  .contact-band__phone { position: absolute; left: 32px; }
  .contact-band__email { position: absolute; left: 365px; }
  .notes__title {
    position: absolute;
    left: 38px;
    top: 50px;
    font-family: "Tinos", "Times New Roman", serif;
    font-weight: 700;
    font-size: 37px;
    line-height: 1.2;
    color: var(--ink-dark);
  }
  .notes__lines {
    position: absolute;
    left: 62px;
    top: 150px;
  }
</style>
</head>
<body>
  <section class="card card--front">
    <div class="sculpture-photo" role="img" aria-label="Photograph of an amethyst geode sculpture on a round granite base"></div>
    <div class="identity">
      <p class="identity__name">Marlo Prewitt</p>
      <p class="identity__studio">Fernvale Craft Works</p>
    </div>
    <div class="contact-band">
      <span class="contact-band__phone">Phone: (555) 213-4098</span>
      <span class="contact-band__email">E-mail: marlo@quillbrookmail.com</span>
    </div>
  </section>

  <section class="card card--back">
    <h2 class="notes__title">Notes</h2>
    <svg class="notes__lines" width="720" height="190" viewBox="0 0 720 190" aria-hidden="true">
      <g stroke="var(--rule)" stroke-width="2" stroke-dasharray="10 16.5">
        <line x1="0" y1="8" x2="720" y2="8"/>
        <line x1="0" y1="96" x2="720" y2="96"/>
        <line x1="0" y1="182" x2="720" y2="182"/>
      </g>
    </svg>
  </section>
</body>
</html>
```